Software Product Website Design

We have a software product which we have just renamed from Milestone Linked Tracking (MLT) to Norvessa. The web site is for www.norvessa-example.com and needs to contain certain information related to our software product in accordance with the information contained in the previous product brochure (see attached). The logo file is also attached but the designer is free to propose alternative logo colours. The theme for the website must be based on the selected logo colours..
Target Market(s)
Project Management, Engineering, Construction etc companies involved with projects in all industries world-wide
Industry/Entity Type
Software
Coding
Coded - Design and coding required
Number of Pages Required
1 page
Font styles to use
Requirements
Must have
- Professional but exciting theme. The contents of the attached brochure should be included.

```html
<!DOCTYPE html>
<html lang="en">
<head>
<meta charset="utf-8">
<title>Norvessa – Progress &amp; Performance Software</title>
<link href="https://fonts.googleapis.com/css2?family=Marcellus&family=Open+Sans:ital,wght@0,400;0,600;0,700;1,700&display=swap" rel="stylesheet">
<style>
:root{
  --red:#d3233a;
  --red-dark:#b01a2e;
  --ink:#2b2b2b;
  --muted:#666;
  --paper:#ffffff;
  --light:#f1f1f1;
  --black:#0d0d0d;
  --grey-icon:#5c5c5c;
  --footer-base:#1a1a1a;
}
*{box-sizing:border-box;margin:0;padding:0}
html,body{width:839px;height:1200px;overflow:hidden;background:var(--paper)}
body{font-family:"Open Sans",Arial,sans-serif;color:var(--ink);font-size:10px;line-height:1.45;position:relative}
a{color:inherit;text-decoration:none}

/* header */
.site-header{height:105px;position:relative;background:var(--paper);border-bottom:1px solid #e4e4e4}
.brand{position:absolute;left:26px;top:22px;display:flex;align-items:center;gap:10px}
.brand-mark{width:44px;height:44px;background:var(--red);border-radius:50%}
.brand-name{font-family:"Open Sans",sans-serif;font-weight:700;font-size:30px;color:var(--red);letter-spacing:.5px}
.top-contact{position:absolute;right:34px;top:12px;text-align:right;font-size:10px;color:var(--muted);line-height:1.7}
.top-contact span{display:inline-flex;align-items:center;gap:5px}
.main-nav{position:absolute;right:28px;top:62px;display:flex;gap:30px;font-size:10px;font-weight:600;letter-spacing:.6px;text-transform:uppercase;color:#444}
.main-nav .active{color:var(--red)}

/* hero */
.hero{position:relative;height:290px;border-bottom:4px solid var(--red)}
.hero-photo{position:absolute;inset:0;background:linear-gradient(115deg,#d9dde2 0%,#9aa3ad 35%,#5d6671 60%,#8b939c 100%)}
.hero-copy{position:absolute;right:34px;top:72px;text-align:right;font-family:"Marcellus",serif;text-transform:uppercase}
.hero-title{color:#fff;font-size:31px;line-height:1.05;text-shadow:0 1px 4px rgba(0,0,0,.35)}
.hero-sub{color:var(--red);font-size:20px;line-height:1.1;margin-top:6px}

/* service icons */
.services{height:106px;display:flex;justify-content:center;gap:72px;padding-top:14px;background:var(--paper)}
.service{display:flex;flex-direction:column;align-items:center;gap:7px;font-size:9px;font-weight:600;letter-spacing:.5px;color:#444;text-transform:uppercase}
.service-icon{width:50px;height:50px;border-radius:50%;background:var(--grey-icon);display:flex;align-items:center;justify-content:center}
.service.featured .service-icon{width:56px;height:56px;background:var(--red);box-shadow:0 0 0 4px #f3c5cc}

/* welcome */
.welcome{height:248px;position:relative;background:var(--light);padding:14px 0 0 28px}
.welcome h1{font-family:"Marcellus",serif;font-weight:400;font-size:24px;color:var(--ink)}
.welcome h1 em{font-family:"Open Sans",sans-serif;font-style:normal;font-weight:700;color:var(--red)}
.welcome-text{width:455px;margin-top:10px;color:#444;font-size:9.5px;line-height:1.55}
.welcome-text p+p{margin-top:10px}
.btn{display:inline-block;background:var(--red);color:#fff;font-size:8px;font-weight:700;text-transform:uppercase;letter-spacing:.5px;padding:5px 10px;margin-top:10px}
.team{position:absolute;right:62px;top:14px;width:220px;height:220px}
.team-photo{width:206px;height:206px;border-radius:50%;border:6px solid #fff;box-shadow:0 0 0 2px #ddd;background:radial-gradient(circle at 50% 40%,#c8ccd2,#7c848d)}
.team-ribbon{position:absolute;left:34px;bottom:28px;width:140px;height:32px;background:var(--red);color:#fff;font-family:"Marcellus",serif;font-size:18px;display:flex;align-items:center;justify-content:center;border-radius:3px}

/* benefits & features */
.highlights{height:253px;background:var(--black);color:#e6e6e6;display:flex;padding:24px 28px 0;gap:40px}
.highlight{flex:1}
.highlight h2{font-family:"Marcellus",serif;font-weight:400;font-size:19px;color:var(--red);margin-bottom:10px}
.highlight ul{list-style:none;font-size:8.6px;line-height:1.75}
.highlight li{position:relative;padding-left:12px}
.highlight li::before{content:"";position:absolute;left:0;top:6px;width:4px;height:4px;background:var(--red)}
.highlight .btn{margin-top:8px}

/* footer */
.site-footer{height:163px;background:linear-gradient(90deg,var(--red-dark),var(--red));color:#fff;position:relative;padding:18px 28px 0;display:flex;gap:50px}
.footer-col h3{font-family:"Marcellus",serif;font-weight:400;font-size:15px;margin-bottom:10px}
.footer-links{list-style:none;font-size:8.5px;line-height:1.9;text-transform:uppercase}
.footer-links li::before{content:"› ";}
.newsletter p{font-size:8.5px;width:160px;line-height:1.5}
.signup{display:flex;margin-top:10px}
.signup span{width:110px;height:18px;background:#fff}
.signup b{background:var(--black);font-size:8px;padding:3px 8px}
.contact-list{list-style:none;font-size:8.5px;line-height:2}
.contact-list li{display:flex;align-items:center;gap:6px}
.footer-brand{position:absolute;right:40px;top:26px;display:flex;flex-direction:column;align-items:center;gap:6px}
.footer-brand .brand-mark{width:60px;height:60px;background:rgba(255,255,255,.25)}
.footer-brand .brand-name{color:#fff;font-size:24px}
.social{position:absolute;right:40px;bottom:14px;display:flex;gap:6px}
.social span{width:16px;height:16px;border-radius:50%;background:rgba(255,255,255,.85)}
.copyright{height:35px;background:var(--footer-base);color:#aaa;font-size:8px;display:flex;align-items:center;padding-left:28px}
</style>
</head>
<body>

<header class="site-header">
  <a class="brand" href="#"><span class="brand-mark"></span><span class="brand-name">norvessa</span></a>
  <div class="top-contact">
    <span><svg width="9" height="9" viewBox="0 0 10 10"><path d="M2 1l2 2-1 1.5c.6 1.2 1.3 1.9 2.5 2.5L7 6l2 2-1.5 1.5C4 9 1 6 .5 2.5z" fill="#d3233a"/></svg>(555) 014 2290</span><br>
    <span><svg width="10" height="8" viewBox="0 0 10 8"><rect x=".5" y=".5" width="9" height="7" fill="none" stroke="#d3233a"/><path d="M.5 .5l4.5 4 4.5-4" fill="none" stroke="#d3233a"/></svg>info@norvessa-example.com</span>
  </div>
  <nav class="main-nav">
    <a class="active" href="#">Home</a><a href="#">Our Company</a><a href="#">Our Product</a><a href="#">Contact Us</a>
  </nav>
</header>

<section class="hero">
  <div class="hero-photo" role="img" aria-label="Photo of hands working over printed progress charts and a tablet"></div>
  <div class="hero-copy">
    <div class="hero-title">Lorem ipsum dolor<br>sit amet,<br>consectetuer</div>
    <div class="hero-sub">Progress &amp;<br>Performance<br>Software</div>
  </div>
</section>

<section class="services">
  <div class="service"><span class="service-icon"><svg width="24" height="24" viewBox="0 0 24 24"><circle cx="12" cy="12" r="9" fill="none" stroke="#fff" stroke-width="2"/><path d="M12 12l5-4" stroke="#fff" stroke-width="2"/></svg></span>Control</div>
  <div class="service"><span class="service-icon"><svg width="24" height="24" viewBox="0 0 24 24"><path d="M3 19l6-6 4 4 8-9" fill="none" stroke="#fff" stroke-width="2"/></svg></span>Improve</div>
  <div class="service featured"><span class="service-icon"><svg width="26" height="26" viewBox="0 0 24 24"><rect x="4" y="3" width="16" height="18" fill="none" stroke="#fff" stroke-width="2"/><path d="M8 9h8M8 13h8M8 17h5" stroke="#fff" stroke-width="2"/></svg></span>Define</div>
  <div class="service"><span class="service-icon"><svg width="24" height="24" viewBox="0 0 24 24"><rect x="4" y="13" width="4" height="7" fill="#fff"/><rect x="10" y="8" width="4" height="12" fill="#fff"/><rect x="16" y="4" width="4" height="16" fill="#fff"/></svg></span>Measure</div>
  <div class="service"><span class="service-icon"><svg width="24" height="24" viewBox="0 0 24 24"><circle cx="10" cy="10" r="6" fill="none" stroke="#fff" stroke-width="2"/><path d="M14.5 14.5l6 6" stroke="#fff" stroke-width="2.5"/></svg></span>Analyze</div>
</section>

<section class="welcome">
  <h1>Welcome To <em>norvessa</em></h1>
  <div class="welcome-text">
    <p>Lorem ipsum dolor sit amet, consectetuer adipiscing elit, sed diam nonummy nibh euismod tincidunt ut laoreet dolore magna aliquam erat volutpat. Ut wisi enim ad minim veniam, quis nostrud exerci tation ullamcorper suscipit lobortis nisl ut aliquip ex ea commodo consequat. Duis autem vel eum iriure dolor in hendrerit in vulputate velit esse molestie consequat.</p>
    <p>Lorem ipsum dolor sit amet, consectetuer adipiscing elit, sed diam nonummy nibh euismod tincidunt ut laoreet dolore magna aliquam erat volutpat. Ut wisi enim ad minim veniam, quis nostrud exerci tation ullamcorper suscipit lobortis nisl ut aliquip...</p>
  </div>
  <a class="btn" href="#">Read More</a>
  <div class="team">
    <div class="team-photo" role="img" aria-label="Group photo of the Norvessa team"></div>
    <div class="team-ribbon">Our Team</div>
  </div>
</section>

<section class="highlights">
  <div class="highlight">
    <h2>Norvessa Benefits</h2>
    <ul>
      <li>Applicable across all industries, sectors and projects</li>
      <li>Significantly reduces the amount of subjectivity</li>
      <li>Promotes structure and discipline</li>
      <li>Information is web based</li>
      <li>Powerful reports (standard formats – untested indicators)</li>
      <li>Setup and management of projects is straightforward</li>
      <li>Facilitates effective resource planning</li>
      <li>Trends are visible within a couple of reporting periods</li>
      <li>Allows project managers to "target" specific problem areas</li>
      <li>Easy to install, configure and customise</li>
    </ul>
    <a class="btn" href="#">Read More</a>
  </div>
  <div class="highlight">
    <h2>Norvessa Features</h2>
    <ul>
      <li>Interactive dashboard based on user preferences</li>
      <li>S-Curves, Pareto Charts, Bulls Eye and Trend Charts</li>
      <li>Tabular reports</li>
      <li>EVM or MLT methods</li>
      <li>Rules of credit and schedule states</li>
      <li>Integration options for meetings, events, roles and actions</li>
      <li>User access restrictions</li>
      <li>Comprehensive and "intelligent" Help Menu</li>
      <li>Change Control functionality</li>
      <li>Integrated Actions and Risk Register</li>
    </ul>
    <a class="btn" href="#">Read More</a>
  </div>
</section>

<footer class="site-footer">
  <div class="footer-col">
    <h3>Quick Links</h3>
    <ul class="footer-links"><li>Home</li><li>Our Company</li><li>Our Product</li><li>Contact Us</li></ul>
  </div>
  <div class="footer-col newsletter">
    <h3>Newsletter Signup</h3>
    <p>Lorem ipsum dolor sit amet, consectetuer adipiscing elit sed diam.</p>
    <div class="signup"><span></span><b>Submit</b></div>
  </div>
  <div class="footer-col">
    <h3>Contact Info</h3>
    <ul class="contact-list">
      <li><svg width="9" height="11" viewBox="0 0 10 12"><path d="M5 0a4 4 0 0 0-4 4c0 3 4 8 4 8s4-5 4-8a4 4 0 0 0-4-4z" fill="#fff"/></svg>12 Harbour Lane, Suite 4, Westford</li>
      <li><svg width="9" height="9" viewBox="0 0 10 10"><path d="M2 1l2 2-1 1.5c.6 1.2 1.3 1.9 2.5 2.5L7 6l2 2-1.5 1.5C4 9 1 6 .5 2.5z" fill="#fff"/></svg>(555) 014 2290</li>
      <li><svg width="10" height="8" viewBox="0 0 10 8"><rect x=".5" y=".5" width="9" height="7" fill="none" stroke="#fff"/><path d="M.5 .5l4.5 4 4.5-4" fill="none" stroke="#fff"/></svg>info@norvessa-example.com</li>
    </ul>
  </div>
  <div class="footer-brand"><span class="brand-mark"></span><span class="brand-name">norvessa</span></div>
  <div class="social"><span></span><span></span><span></span><span></span></div>
</footer>

<div class="copyright">Copyright 2015 © Norvessa Ltd | All Rights Reserved</div>

</body>
</html>
```